Maple Hollow Canine Massage Needs a Business Card Design

Maple Hollow Canine Massage is a new therapeutic canine massage company located in Nederland, Colorado. I need a business card design that include my logo and basic contact information.

Target Market(s)

Pet owners, veterinarians

Industry/Entity Type

Business

Contact Information for Business Card

Lydia Ferrow, CCMT
303.518.7269
lydia@maplehollowmassage.example
www.maplehollowmassage.example

Colors
6c459b
886aae
b8a6cd
a64599
b768aa
d3a5cc
fbed22

Requirements
Must have
• Font should be similar to font in logo.

```html
<!DOCTYPE html>
<html lang="en">
<head>
<meta charset="utf-8">
<title>Maple Hollow Canine Massage – Business Card</title>
<link href="https://fonts.googleapis.com/css2?family=Source+Sans+3:wght@400;600&display=swap" rel="stylesheet">
<style>
  :root {
    --page-bg: #d9d4d0;
    --card-frost-top: #f1eef0;
    --card-frost-bottom: #e4dfe3;
    --card-edge: #ffffff;
    --purple-deep: #6c459b;
    --purple-mid: #886aae;
    --magenta: #a64599;
    --gold: #dcae2e;
    --ink: #3a2f44;
  }
  html, body {
    margin: 0;
    padding: 0;
    width: 1200px;
    height: 969px;
    overflow: hidden;
    background: var(--page-bg);
    font-family: "Source Sans 3", "Helvetica Neue", Arial, sans-serif;
  }
  .card {
    position: absolute;
    left: 80px;
    top: 188px;
    width: 1040px;
    height: 592px;
    border-radius: 34px;
    overflow: hidden;
    box-shadow: 0 14px 40px rgba(60, 40, 70, 0.18);
  }
  .card-art {
    position: absolute;
    inset: 0;
  }
  .contact {
    position: absolute;
    left: 66px;
    top: 360px;
    color: var(--ink);
  }
  .contact-name {
    margin: 0 0 14px;
    font-size: 36px;
    font-weight: 600;
    letter-spacing: 0.2px;
  }
  .contact-name .credential {
    font-size: 26px;
    font-weight: 400;
  }
  .contact-list {
    list-style: none;
    margin: 0;
    padding: 0;
  }
  .contact-list li {
    display: flex;
    align-items: center;
    gap: 14px;
    font-size: 26px;
    line-height: 40px;
  }
  .contact-list svg {
    width: 22px;
    height: 22px;
    fill: var(--ink);
    flex: none;
  }
  .brand-text {
    position: absolute;
    left: 666px;
    top: 72px;
    width: 304px;
    height: 304px;
    display: flex;
    flex-direction: column;
    align-items: center;
    justify-content: center;
    text-align: center;
    color: var(--gold);
    font-size: 30px;
    font-weight: 600;
    line-height: 1.15;
    letter-spacing: 1px;
    text-transform: uppercase;
  }
</style>
</head>
<body>
  <div class="card">
    <svg class="card-art" width="1040" height="592" viewBox="0 0 1040 592" aria-hidden="true">
      <defs>
        <linearGradient id="frost" x1="0" y1="0" x2="0" y2="1">
          <stop offset="0" stop-color="var(--card-frost-top)"/>
          <stop offset="1" stop-color="var(--card-frost-bottom)"/>
        </linearGradient>
        <linearGradient id="feature-fill" x1="0" y1="0" x2="1" y2="1">
          <stop offset="0" stop-color="#9b6fb8"/>
          <stop offset="0.55" stop-color="#b48ac6"/>
          <stop offset="1" stop-color="#d3b6de"/>
        </linearGradient>
      </defs>
      <rect class="card-base" x="0" y="0" width="1040" height="592" rx="34" fill="url(#frost)"/>
      <circle class="feature-ring" cx="295" cy="452" r="306" fill="none" stroke="var(--gold)" stroke-width="7"/>
      <circle class="feature-disc" cx="295" cy="452" r="298" fill="url(#feature-fill)"/>
      <circle class="brand-disc" cx="818" cy="224" r="152" fill="var(--purple-deep)"/>
      <rect x="1.5" y="1.5" width="1037" height="589" rx="33" fill="none" stroke="var(--card-edge)" stroke-opacity="0.8" stroke-width="3"/>
    </svg>

    <div class="brand-text">Maple Hollow<br>Canine Massage</div>

    <div class="contact">
      <p class="contact-name">Lydia Ferrow, <span class="credential">CCMT</span></p>
      <ul class="contact-list">
        <li>
          <svg viewBox="0 0 24 24" aria-hidden="true"><path d="M6.6 10.8a15.1 15.1 0 0 0 6.6 6.6l2.2-2.2c.3-.3.7-.4 1-.2 1.1.4 2.3.6 3.6.6.6 0 1 .4 1 1V20c0 .6-.4 1-1 1A17 17 0 0 1 3 4c0-.6.4-1 1-1h3.5c.6 0 1 .4 1 1 0 1.3.2 2.5.6 3.6.1.3 0 .7-.2 1z"/></svg>
          303.518.7269
        </li>
        <li>
          <svg viewBox="0 0 24 24" aria-hidden="true"><path d="M2 5h20v14H2zm2 2v.4l8 5 8-5V7zm0 2.8V17h16V9.8l-8 5z"/></svg>
          lydia@maplehollowmassage.example
        </li>
        <li>
          <svg viewBox="0 0 24 24" aria-hidden="true"><path d="M12 2a10 10 0 1 0 0 20 10 10 0 0 0 0-20zm6.9 6h-3a15 15 0 0 0-1.3-3.9A8 8 0 0 1 18.9 8zM12 4c.8 1.2 1.5 2.5 1.9 4h-3.8c.4-1.5 1.1-2.8 1.9-4zM4.3 14a8 8 0 0 1 0-4h3.4a16 16 0 0 0 0 4zm.8 2h3a15 15 0 0 0 1.3 3.9A8 8 0 0 1 5.1 16zm3-8h-3a8 8 0 0 1 4.3-3.9A15 15 0 0 0 8.1 8zM12 20c-.8-1.2-1.5-2.5-1.9-4h3.8c-.4 1.5-1.1 2.8-1.9 4zm2.3-6H9.7a14 14 0 0 1 0-4h4.6a14 14 0 0 1 0 4zm.3 5.9a15 15 0 0 0 1.3-3.9h3a8 8 0 0 1-4.3 3.9zm1.7-5.9a16 16 0 0 0 0-4h3.4a8 8 0 0 1 0 4z"/></svg>
          www.maplehollowmassage.example
        </li>
      </ul>
    </div>
  </div>
</body>
</html>
```